A Maple Syrup Label for a Local Buniness

We are looking for a label for our maple syrup business. Our business currently sells honey, and we are expanding into maple syrup. Our Business name is "Brackley Honey" and we currently have a logo attached below. We would like to incorporate the bee and BH part, but the label could also read "Brackley Farms" with the words maple syrup. We do not want consumers to confuse the maple syrup jars with the honey jars. It should be clear that the jars contain maple syrup. We are open to new designs as well.

```html
<!DOCTYPE html>
<html lang="en">
<head>
<meta charset="utf-8">
<title>Brackley Farms Maple Syrup Label</title>
<link rel="stylesheet" href="https://fonts.googleapis.com/css2?family=Cinzel:wght@700&family=Marcellus&family=Montserrat:wght@600&display=swap">
<style>
  :root {
    --page: #ffffff;
    --label-black: #000000;
    --gold: #f5b800;
    --white: #ffffff;
    --leaf-red: #2a0303;
  }
  html, body {
    margin: 0;
    padding: 0;
    width: 1200px;
    height: 767px;
    overflow: hidden;
    background: var(--page);
  }
  .canvas {
    position: relative;
    width: 1200px;
    height: 767px;
  }
  .label {
    position: absolute;
    left: 319px;
    top: 48px;
    width: 660px;
    height: 788px;
    transform: scale(0.85);
    transform-origin: top left;
  }
  .label-shape {
    position: absolute;
    inset: 0;
  }
  .brand-placeholder {
    position: absolute;
    left: 0;
    top: 190px;
    width: 660px;
    display: flex;
    align-items: center;
    justify-content: center;
    gap: 14px;
  }
  .brand-placeholder-dot {
    width: 16px;
    height: 16px;
    border-radius: 50%;
    background: var(--gold);
  }
  .brand-placeholder-name {
    font-family: "Marcellus", serif;
    font-size: 32px;
    line-height: 1;
    color: var(--gold);
  }
  .farm-name {
    position: absolute;
    left: 0;
    width: 660px;
    text-align: center;
    font-family: "Marcellus", serif;
    font-size: 72px;
    line-height: 1;
    margin: 0;
    font-weight: 400;
  }
  .farm-name--first { top: 312px; color: var(--white); }
  .farm-name--second { top: 385px; color: var(--gold); }
  .divider {
    position: absolute;
    left: 88px;
    width: 484px;
    height: 2px;
    background: var(--gold);
  }
  .divider--top { top: 500px; }
  .divider--bottom { top: 606px; }
  .product-name {
    position: absolute;
    top: 528px;
    left: 0;
    width: 660px;
    text-align: center;
    font-family: "Cinzel", serif;
    font-weight: 700;
    font-size: 42px;
    letter-spacing: 4px;
    color: var(--white);
    margin: 0;
  }
  .usage-notes {
    position: absolute;
    top: 656px;
    left: 0;
    width: 660px;
    text-align: center;
    font-family: "Montserrat", sans-serif;
    font-weight: 600;
    font-size: 16px;
    line-height: 25px;
    letter-spacing: 1.5px;
    color: var(--white);
    margin: 0;
  }
</style>
</head>
<body>
<main class="canvas">
  <section class="label">
    <svg class="label-shape" viewBox="0 0 660 788" width="660" height="788">
      <defs>
        <radialGradient id="leafField" cx="50%" cy="45%" r="60%">
          <stop offset="0%" stop-color="#000000"/>
          <stop offset="70%" stop-color="#0d0000"/>
          <stop offset="100%" stop-color="#2a0303"/>
        </radialGradient>
      </defs>
      <path d="M0,290 C0,120 150,0 330,0 C510,0 660,120 660,290 L625,772 Q624,788 608,788 L52,788 Q36,788 35,772 Z" fill="var(--label-black)"/>
      <path role="img" aria-label="Scattered dark red maple leaves on black" d="M30,300 C30,140 170,32 330,32 C490,32 630,140 630,300 L598,738 Q596,756 578,756 L82,756 Q64,756 62,738 Z" fill="url(#leafField)" stroke="var(--gold)" stroke-width="7"/>
    </svg>

    <div class="brand-placeholder">
      <span class="brand-placeholder-dot"></span>
      <span class="brand-placeholder-name">Brackley Honey</span>
    </div>

    <h1 class="farm-name farm-name--first">BRACKLEY</h1>
    <p class="farm-name farm-name--second">FARMS</p>

    <span class="divider divider--top"></span>
    <h2 class="product-name">MAPLE SYRUP</h2>
    <span class="divider divider--bottom"></span>

    <p class="usage-notes">TOP TO OPEN<br>REFRIGERATE AFTER OPEN<br>6.8Oz / 200ml</p>
  </section>
</main>
</body>
</html>
```